Hip Surgeon needs a web page re-design.

I have a web page to provide information about the diseases of the hip joint for the patients from my private practice since 2008. I need a re-design job for a fresh new look.
We have made a new logo and a new stationery design here in Marqueloft (please see the uploaded files) and I want to make my web page look-alike the new design concepts.
I like the color blue and tones of blue, matching my logo and stationery.
I don't like "busy" designs. It must be clean, elegant and ease to read. The final design should be "mobile friendly" if possible.
Please visit my website www.vilacorendasul.com.br to take a look and get some inspiration.

```html
<!DOCTYPE html>
<html lang="en">
<head>
<meta charset="utf-8">
<title>Dr. Rafael M. Antunes – Cirurgia do Quadril</title>
<link href="https://fonts.googleapis.com/css2?family=Montserrat:wght@400;500;600&family=Open+Sans:wght@400;600&family=Roboto+Condensed:wght@400&display=swap" rel="stylesheet">
<style>
  :root{
    --blue:#1e8fd6;
    --blue-dark:#1565b0;
    --nav-top:#2bb6ee;
    --nav-bottom:#1a9fe0;
    --navy:#1d3f7a;
    --text:#666;
    --heading:#111;
    --rule:#e2e2e2;
    --footer-top:#2590e0;
    --footer-bottom:#1a66c4;
    --footer-muted:#bfe0fb;
  }
  *{box-sizing:border-box;margin:0;padding:0}
  html,body{width:1079px;height:1200px;overflow:hidden;background:#fff}
  body{position:relative;font-family:"Open Sans",sans-serif;color:var(--text)}
  .page{position:absolute;left:89px;top:0;width:903px;height:1107px;background:#fff;box-shadow:0 0 18px rgba(0,0,0,.12)}
  .header{position:absolute;left:0;top:0;width:100%;height:106px}
  .brand{position:absolute;left:24px;top:27px;display:flex;align-items:center;gap:10px}
  .brand-mark{width:62px;height:62px;border-radius:50%;background:var(--blue)}
  .brand-name{font-family:"Roboto Condensed",sans-serif;font-size:29px;line-height:30px;color:var(--blue)}
  .brand-tag{font-family:"Roboto Condensed",sans-serif;font-size:21px;line-height:24px;color:var(--blue)}
  .appointment{position:absolute;right:29px;top:42px;text-align:right;font-family:"Montserrat",sans-serif}
  .appointment-label{font-size:14px;color:#555}
  .appointment-phone{font-size:23px;color:var(--blue-dark);margin-top:2px}
  .nav{position:absolute;left:0;top:106px;width:100%;height:49px;background:linear-gradient(var(--nav-top),var(--nav-bottom));display:flex;align-items:center;justify-content:space-around;padding:0 18px;font-family:"Montserrat",sans-serif;font-weight:500;font-size:14px;color:#fff}
  .hero{position:absolute;left:0;top:155px;width:100%;height:364px;background:linear-gradient(180deg,#cfe3ee 0%,#e8e0cc 40%,#b07f4f 72%,#5b4333 100%)}
  .hero-caption{position:absolute;left:31px;top:111px;width:355px;height:147px;background:rgba(20,90,140,.85);border-radius:3px;padding:22px 24px 0;font-family:"Montserrat",sans-serif;white-space:nowrap}
  .hero-kicker{font-size:22px;color:#3fbaf2;line-height:26px}
  .hero-title{font-size:27px;color:#fff;line-height:32px}
  .hero-text{font-family:"Open Sans",sans-serif;font-size:11px;color:#e6f1f8;line-height:17px;margin-top:10px;white-space:normal}
  .hero-dots{position:absolute;left:421px;top:340px;display:flex;gap:5px}
  .hero-dots span{width:11px;height:11px;border-radius:50%;background:#fff}
  .feature{position:absolute;top:541px;width:281px}
  .feature-media{height:111px}
  .feature-title{font-family:"Montserrat",sans-serif;font-weight:400;font-size:17px;color:var(--blue);margin-top:9px;line-height:22px}
  .feature-text{font-size:10px;line-height:17px;margin-top:3px}
  .read-more{display:inline-block;font-family:"Montserrat",sans-serif;font-weight:600;font-size:13.5px;color:var(--navy);margin-top:8px;text-decoration:none}
  .divider{position:absolute;left:13px;top:793px;width:870px;border-top:1px solid var(--rule)}
  .welcome{position:absolute;left:13px;top:849px;width:540px}
  .welcome-title{font-family:"Montserrat",sans-serif;font-weight:500;font-size:21px;color:var(--heading);letter-spacing:-.3px;white-space:nowrap}
  .welcome-lead{font-size:14.5px;color:#555;margin-top:10px}
  .welcome-text{font-size:11.5px;line-height:19px;margin-top:5px;width:505px}
  .video{position:absolute;left:574px;top:843px;width:292px;height:185px;border:1px solid #ccc;border-radius:3px;background:linear-gradient(135deg,#d8d8d8,#9a9a9a 55%,#c98a8a 62%,#e8e8e8)}
  .video-play{position:absolute;left:128px;top:76px}
  .footer{position:absolute;left:0;top:1107px;width:1079px;height:93px;background:linear-gradient(var(--footer-top),var(--footer-bottom))}
  .footer-nav{position:absolute;left:109px;top:25px;font-family:"Montserrat",sans-serif;font-weight:500;font-size:12.5px;color:#fff}
  .footer-nav .sep{margin:0 4px}
  .footer-copy{position:absolute;left:109px;top:49px;font-size:11px;color:var(--footer-muted)}
  .social{position:absolute;right:116px;top:21px;display:flex;gap:6px}
  .social span{width:22px;height:22px;border-radius:50%;background:#fff}
</style>
</head>
<body>
  <div class="page">
    <header class="header">
      <div class="brand">
        <div class="brand-mark"></div>
        <div>
          <div class="brand-name">Dr. Rafael M. Antunes</div>
          <div class="brand-tag">Cirurgia do Quadril</div>
        </div>
      </div>
      <div class="appointment">
        <div class="appointment-label">Make an appointment Now</div>
        <div class="appointment-phone">(555) 304-2190</div>
      </div>
    </header>
    <nav class="nav">
      <span>HOME</span><span>ABOUT US</span><span>SERVICES</span><span>LINKS</span><span>DOWNLOADS</span><span>ATUALIDADES</span><span>CONTACT US</span>
    </nav>
    <section class="hero" role="img" aria-label="Photo of a runner resting on a sunlit track beside a wooden fence">
      <div class="hero-caption">
        <div class="hero-kicker">Duis tincidunt lectus quis</div>
        <div class="hero-title">Suspendisse vulputate</div>
        <p class="hero-text">Pellentesque habitant morbi tristique senectus et netus et malesuada fames ac turpis egest</p>
      </div>
      <div class="hero-dots"><span></span><span></span><span></span><span></span></div>
    </section>

    <article class="feature" style="left:15px">
      <div class="feature-media" role="img" aria-label="Doctor with a digital anatomy display" style="background:linear-gradient(135deg,#cfe8f7,#9fd2ef)"></div>
      <h3 class="feature-title">Treatment &amp; Care</h3>
      <p class="feature-text">Phasellus felis dolor scelerisque a tempus eget lobortis id libero Donec scelerisque leo ac risus Praesent</p>
      <a class="read-more">Read More ›</a>
    </article>
    <article class="feature" style="left:309px">
      <div class="feature-media" role="img" aria-label="Couple stretching outdoors" style="background:linear-gradient(135deg,#3a9fd8,#c9a86a 60%,#7a6a4a)"></div>
      <h3 class="feature-title">Services We Provide</h3>
      <p class="feature-text">Phasellus felis dolor scelerisque a tempus eget lobortis id libero Donec scelerisque leo ac risus Praesent</p>
      <a class="read-more">Read More ›</a>
    </article>
    <article class="feature" style="left:607px">
      <div class="feature-media" role="img" aria-label="Cyclists riding a mountain road" style="background:linear-gradient(180deg,#3f7fc4,#9ab6c8 55%,#5f8a3a)"></div>
      <h3 class="feature-title">What We Do</h3>
      <p class="feature-text">Phasellus felis dolor scelerisque a tempus eget lobortis id libero Donec scelerisque leo ac risus Praesent</p>
      <a class="read-more">Read More ›</a>
    </article>

    <div class="divider"></div>

    <section class="welcome">
      <h2 class="welcome-title">WELCOME TO DR. RAFAEL MOREIRA ANTUNES</h2>
      <p class="welcome-lead">Morbi eget arcu Morbi porta libero id ullamcorper nonummy nibh</p>
      <p class="welcome-text">Phasellus felis dolor scelerisque a tempus eget lobortis id libero Donec scelerisque leo ac risus Praesent sit amet est In dictum dolor eu dictum porttitor enim felis viverra mi eget luctus massa purus quis odio Etiam nulla massa pharetra facilisis volutpat in imperdiet</p>
      <p class="welcome-text" style="margin-top:10px">Sit amet sem Aliquam nec erat at purus cursus interdum Vestibulum ligula augue bibendum accumsan vestibulum ut commodo a mi Morbi ornare gravida .</p>
    </section>

    <div class="video" role="img" aria-label="Video: hands pressing on a painful lower back">
      <svg class="video-play" width="34" height="34" viewBox="0 0 34 34"><circle cx="17" cy="17" r="16" fill="#222" stroke="#fff" stroke-width="2"/><path d="M13 10l11 7-11 7z" fill="#fff"/></svg>
    </div>
  </div>

  <footer class="footer">
    <div class="footer-nav">HOME<span class="sep">|</span>ABOUT US<span class="sep">|</span>SERVICES<span class="sep">|</span>LINKS<span class="sep">|</span>DOWNLOADS<span class="sep">|</span>ATUALIDADES<span class="sep">|</span>CONTACT US</div>
    <div class="footer-copy">© 2014 Company Name.&nbsp; All right reserved.&nbsp; Term of Use</div>
    <div class="social"><span></span><span></span><span></span></div>
  </footer>
</body>
</html>
```